High-end construction company needs a business card design

We need a modern looking business card that draws people in, is memorable and looks so good people will want to sick it on their fridges.
On the first side what is needed are:
Logo
My name - Tomas Verbelk
Title - Managing Director
Website - www.kravel.co.uk
Email - tomas@kravel.co.uk
Telephone - 020 5194 6381
Mobile - 07845319027
On the back side was is needed is a list of all the services we provide:
-Kitchen Renovations
-Bathroom Renovations
-House Renovations
-Garage Conversions
-Extensions
-Loft Conversions
-Conservatories
-Carpentry
-Tiling
-Electrical
-Plumbing & Heating
-Bricklaying
-Landscaping
-Decorating
-Plastering
We would like the colours to be the same shades as on the logo with grey or black for the words.
Target Market(s)
Anyone who needs building work done
Contact Information for Business Card
This business card is for a construction company which strives to deliver excellent service and quality.
The look and feel of the card should represent this.
Requirements
Must have
- On the first side what is needed are:
Logo
My name - Tomas Verbelk
Title - Managing Director
Website - www.kravel.co.uk
Email - tomas@kravel.co.uk
Telephone - 020 5194 6381
Mobile - 07845319027
Nice to have
- Cool looking features

```html
<!DOCTYPE html>
<html lang="en">
<head>
<meta charset="utf-8">
<title>Kravel Construction Ltd – Business Card</title>
<link href="https://fonts.googleapis.com/css2?family=Poppins:wght@400;500;600;700&display=swap" rel="stylesheet">
<style>
  :root {
    --stage: #2c2c2e;
    --green-dark: #3f8a3d;
    --green-mid: #4f9d48;
    --green-light: #6cbf45;
    --green-pale: #9bd66b;
    --ink: #4a4a4a;
    --paper: #ffffff;
  }
  * { box-sizing: border-box; margin: 0; padding: 0; }
  html, body {
    width: 1200px; height: 960px; overflow: hidden;
    background: var(--stage);
    font-family: "Poppins", sans-serif;
  }
  .stage {
    position: relative; width: 1200px; height: 960px;
    display: flex; flex-direction: column; align-items: center; justify-content: center; gap: 36px;
  }
  .card {
    position: relative; width: 800px; height: 430px; overflow: hidden;
    border-radius: 4px;
    box-shadow: 0 14px 30px rgba(0,0,0,.45);
  }

  /* Services side */
  .card--services {
    background: linear-gradient(135deg, var(--green-light) 0%, var(--green-mid) 45%, var(--green-dark) 100%);
    color: var(--paper);
    display: flex; flex-direction: column; align-items: center; padding-top: 70px;
  }
  .brand {
    font-weight: 700; letter-spacing: 1px; text-transform: uppercase; line-height: 1.05; text-align: center;
  }
  .brand__name { display: block; font-size: 64px; letter-spacing: 4px; }
  .brand__suffix { display: block; font-size: 19px; letter-spacing: 5px; }
  .card--services .brand { color: var(--paper); }
  .services-label {
    display: flex; align-items: center; gap: 16px; width: 560px;
    margin-top: 28px; color: var(--green-pale);
    font-weight: 600; font-size: 22px; letter-spacing: 2px; text-transform: uppercase;
  }
  .services-label::before, .services-label::after {
    content: ""; flex: 1; height: 2px; background: var(--green-pale);
  }
  .services-list {
    list-style: none; margin-top: 16px; width: 640px;
    display: flex; flex-wrap: wrap; justify-content: center; gap: 2px 0;
    font-size: 19px; font-weight: 500; line-height: 1.45;
  }
  .services-list li { padding: 0 7px; }
  .services-list li::before {
    content: ""; display: inline-block; width: 6px; height: 6px; border-radius: 50%;
    background: var(--green-pale); margin-right: 7px; vertical-align: middle;
  }

  /* Contact side */
  .card--contact { background: var(--paper); }
  .card--contact .brand {
    position: absolute; left: 50px; top: 150px; width: 330px; color: var(--green-light);
  }
  .card--contact .brand__name { font-size: 62px; }
  .card--contact .brand__suffix { font-size: 18px; }
  .divider {
    position: absolute; left: 410px; top: 70px; width: 2px; height: 270px; background: var(--green-light);
  }
  .contact {
    position: absolute; left: 440px; top: 70px; color: var(--ink);
    font-size: 20px; line-height: 1.4;
  }
  .contact__name {
    color: var(--green-mid); font-weight: 700; font-size: 30px; text-transform: uppercase; letter-spacing: .5px; line-height: 1.15;
  }
  .contact__title { font-size: 20px; margin-bottom: 10px; }
  .contact__address { margin-bottom: 10px; }
  .contact__lines { list-style: none; }
  .contact__lines li { display: flex; align-items: center; gap: 10px; }
  .contact__lines svg { width: 18px; height: 18px; fill: var(--green-light); flex: none; }
  .band {
    position: absolute; left: 0; bottom: 0; width: 100%; height: 16px; display: flex;
  }
  .band__light { flex: 0 0 64%; background: var(--green-light); }
  .band__dark { flex: 1; background: var(--green-dark); margin-left: 3px; }
</style>
</head>
<body>
<main class="stage">

  <section class="card card--services" aria-label="Services side">
    <div class="brand">
      <span class="brand__name">Kravel</span>
      <span class="brand__suffix">Construction Ltd</span>
    </div>
    <h2 class="services-label">Services</h2>
    <ul class="services-list">
      <li>Kitchen Renovations</li><li>Bathroom Renovations</li><li>House Renovations</li>
      <li>Garage Conversions</li><li>Extensions</li><li>Loft Conversions</li><li>Conservatories</li>
      <li>Carpentry</li><li>Tiling</li><li>Electrical</li><li>Plumbing &amp; Heating</li>
      <li>Bricklaying</li><li>Landscaping</li><li>Decorating</li><li>Plastering</li>
    </ul>
  </section>

  <section class="card card--contact" aria-label="Contact side">
    <div class="brand">
      <span class="brand__name">Kravel</span>
      <span class="brand__suffix">Construction Ltd</span>
    </div>
    <div class="divider"></div>
    <div class="contact">
      <h1 class="contact__name">Tomas Verbelk</h1>
      <p class="contact__title">Managing Director</p>
      <p class="contact__address">48-50 Harlow Street<br>London, E2 9PQ</p>
      <ul class="contact__lines">
        <li><svg viewBox="0 0 24 24"><path d="M6.6 10.8a15.1 15.1 0 0 0 6.6 6.6l2.2-2.2a1 1 0 0 1 1-.25 11.4 11.4 0 0 0 3.6.57 1 1 0 0 1 1 1V20a1 1 0 0 1-1 1A17 17 0 0 1 3 4a1 1 0 0 1 1-1h3.5a1 1 0 0 1 1 1c0 1.25.2 2.45.57 3.57a1 1 0 0 1-.25 1z"/></svg>020 5194 6381</li>
        <li><svg viewBox="0 0 24 24"><path d="M8 1h8a2 2 0 0 1 2 2v18a2 2 0 0 1-2 2H8a2 2 0 0 1-2-2V3a2 2 0 0 1 2-2zm0 3v14h8V4zm4 15.5a1 1 0 1 0 0 2 1 1 0 0 0 0-2z"/></svg>07845319027</li>
        <li><svg viewBox="0 0 24 24"><path d="M2 5h20v14H2zm2 2v.5l8 5 8-5V7zm0 2.8V17h16V9.8l-8 5z"/></svg>tomas@kravel.co.uk</li>
        <li><svg viewBox="0 0 24 24"><path d="M12 2a10 10 0 1 0 0 20 10 10 0 0 0 0-20zm6.9 6h-3a15 15 0 0 0-1.3-3.9A8 8 0 0 1 18.9 8zM12 4c.8 1.2 1.5 2.5 1.9 4h-3.8c.4-1.5 1.1-2.8 1.9-4zM4.3 14a8 8 0 0 1 0-4h3.4a16 16 0 0 0 0 4zm.8 2h3a15 15 0 0 0 1.3 3.9A8 8 0 0 1 5.1 16zm3-8h-3a8 8 0 0 1 4.3-3.9A15 15 0 0 0 8.1 8zM12 20c-.8-1.2-1.5-2.5-1.9-4h3.8c-.4 1.5-1.1 2.8-1.9 4zm2.3-6H9.7a14 14 0 0 1 0-4h4.6a14 14 0 0 1 0 4zm.3 5.9a15 15 0 0 0 1.3-3.9h3a8 8 0 0 1-4.3 3.9zm1.7-5.9a16 16 0 0 0 0-4h3.4a8 8 0 0 1 0 4z"/></svg>www.kravel.co.uk</li>
      </ul>
    </div>
    <div class="band"><span class="band__light"></span><span class="band__dark"></span></div>
  </section>

</main>
</body>
</html>
```